依頼詳細
上記に記載したアドバイスシートのベースを作成していただきたいです。内容は、顧客別に写真を入れたり、文字を入れたりするので、データで納品していただきたいです。30代、40代がメインターゲットで、おしゃれで少しラグジュアリーかつ女性らしいデザインを希望します。
内容や順番などこちらも変更する可能性があります。現在使っているアドバイスシートを参考にオシャレに、気分が上がるような仕上がりにしていただくのが希望です。 通常、初回の体験を受けていただいたお客様にはレッスンに進む方も多いのですが、こちらの方々にもノートというか、教科書のようなものを今後作成したいと思っているので、今回のデザインとも統一感を持たせたいと思っているので、お願いする可能性もあるかもしれません。
サイズ
A4
ページ数
10ページ
希望イメージ
シンプル 複雑
単色 カラフル
暗い 明るい
日常 高級
遊び心 厳粛
未来的 伝統的
女性的 男性的
希望する色
メイクアップと言って想像するような色、単色よりは数色使ってバランスの良い感じ
納品ファイル
補足説明
添付しているものが現在使用しているアドバイスシートです。これにもっと情報を追加していきたいので、添付しているものよりページ数などは増えると思います。(追加する文章や情報などは現在作成中です) 。デザインや、文字の配置、分かりやすさなどを追求したいので、そのあたりはアドバイスをいただけると有り難いです。現在、ベースのアドバイスシートをgood notesに取り込んで、iPadで文字と写真、写真への書き加えはペンで書き加えています。ですがこの作業が結構時間がかかって仕事量として重たいので、何かいいやり方があればそれもアドバイスいただけると嬉しいです。
内容は何度もやりとりして修正させていただく可能性があるので、一旦大幅であっても、早めに出していただけると決めやすいです。・最初のデザインの全体的な雰囲気や、ご提案者様の過去の事例など見させていただき雰囲気を決めさせていただきたいです。・あと、こちらからの希望になるべく沿っていただけるようやりとりしていただける方がとても有り難いです。当方今月より産休に入っており、日中も時間は割とあるので、ご対応していただけると助かります。(募集最終日頃にかなり決めた形で作り込んで応募される方よりは、最初はラフな形から今後柔軟に対応していただける方の方がありがたいです) 基本は作成枚数によって価格を決めさせていただきたいと思っています。現状より増える可能性が高いので、価格は上がる可能性があります。
ご応募ありがとうございます。追加修正の依頼を記載いたします。
【現在依頼しているページについて】
・ビフォーアフターや、各種メイク工程のページについて、文字量が多くみづらいのが難点で、もう少しグラフや表を入れて可視化したいです。(アイディアがあればお願いします) 添付PDF1枚目

【追加ページについて】
・お悩みとなりたいイメージを記載するページ(こちらも表やグラフなどで可視化できる案があればありがたいです)添付PDF2枚目

・添付PDF3枚目
利用サービスの流れを可視化できるページを作成したいです

・添付PDF4枚目
サロンの情報へアクセスできるよう情報をまとめたページ

今後メイクやスキンケア販売をしたい方へ向けての告知ページ

一旦以上になります。
すみません。募集が終了した場合添付ができないかもしれず、現在調べております。もしできない場合は、選定させていただき、個別にご連絡させていただきます。
可能な場合はPDF添付させていただきます。

依頼に加え、提案などしていただいたのでとても有り難かったです。

皆様とても魅力的なご提案ばかりで、ギリギリまで選定できず申し訳ございませんでした。今回は1社に決めさせていただいたのですが、素敵なご提案ばかりで、お願いして良かったなと思いました。こちらのご提案にお時間や尽力を割いていただいてありがとうございました。また機会ありましたらよろしくお願いいたします。

```html
<!DOCTYPE html>
<html lang="ja">
<head>
<meta charset="utf-8">
<title>骨格分析 make advice sheet</title>
<link rel="stylesheet" href="https://fonts.googleapis.com/css2?family=Shippori+Mincho:wght@400;500&family=Cormorant+Garamond:wght@400;500&display=swap">
<style>
  :root {
    --paper: #ffffff;
    --frame-light: #e9a3a0;
    --frame-mid: #d98581;
    --frame-deep: #c96e6b;
    --ink: #c4706d;
    --ink-soft: #b97a77;
    --rule: #dfa3a0;
    --logo-ink: #3b3535;
  }
  * { margin: 0; padding: 0; box-sizing: border-box; }
  html, body { width: 846px; height: 1200px; overflow: hidden; background: var(--paper); }
  .sheet {
    position: relative;
    width: 846px;
    height: 1200px;
    background: var(--paper);
    font-family: "Shippori Mincho", serif;
    color: var(--ink);
  }
  .frame {
    position: absolute;
    left: 34px; top: 22px;
    width: 776px; height: 1046px;
    background:
      radial-gradient(ellipse at 20% 10%, rgba(255,255,255,0.18), transparent 45%),
      radial-gradient(ellipse at 85% 90%, rgba(160,70,70,0.18), transparent 50%),
      linear-gradient(160deg, var(--frame-light), var(--frame-mid) 55%, var(--frame-deep));
  }
  .panel {
    position: absolute;
    left: 68px; top: 72px;
    width: 694px; height: 972px;
    background: var(--paper);
  }
  .title {
    position: absolute;
    left: 0; top: 22px; width: 100%;
    text-align: center;
    line-height: 1;
  }
  .title-ja { font-size: 34px; letter-spacing: 8px; font-weight: 500; }
  .title-en {
    display: block; margin-top: 8px;
    font-family: "Cormorant Garamond", serif;
    font-size: 22px; letter-spacing: 3px;
  }
  .sheet-no {
    position: absolute; right: 52px; top: 34px;
    font-family: "Cormorant Garamond", serif;
    font-size: 28px;
  }
  .sheet-no strong { font-size: 40px; font-weight: 400; }
  .rule { position: absolute; left: 0; width: 100%; height: 1px; background: var(--rule); }
  .rule-top { top: 114px; }
  .rule-name { top: 165px; }
  .client-name {
    position: absolute; right: 18px; top: 126px;
    font-size: 22px;
  }
  .photo-grid {
    position: absolute; left: 0; top: 165px;
    width: 100%; height: 496px;
    border-bottom: 1px solid var(--rule);
  }
  .photo-slot { position: absolute; }
  .photo-slot .label {
    position: absolute; left: 14px; top: 12px;
    font-family: "Cormorant Garamond", serif; font-size: 22px;
  }
  .slot-a { left: 0; top: 0; width: 423px; height: 100%; border-right: 1px solid var(--rule); }
  .slot-b { left: 423px; top: 0; width: 271px; height: 243px; border-bottom: 1px solid var(--rule); }
  .slot-c { left: 423px; top: 243px; width: 271px; height: 253px; }
  .notes { position: absolute; left: 18px; font-size: 20px; letter-spacing: 2px; }
  .notes .key { font-family: "Cormorant Garamond", serif; font-size: 24px; margin-right: 4px; }
  .note-whole { top: 680px; }
  .note-right { top: 800px; }
  .note-left { top: 878px; }
  .footer-tag {
    position: absolute; right: 42px; top: 1070px;
    font-family: "Cormorant Garamond", serif; font-size: 15px; color: var(--ink-soft);
  }
  .brand {
    position: absolute; left: 0; top: 1092px; width: 100%;
    text-align: center; color: var(--logo-ink);
  }
  .brand-name {
    font-family: "Cormorant Garamond", serif;
    font-size: 24px; letter-spacing: 2px;
  }
  .brand-line {
    display: block; margin-top: 2px;
    font-family: "Cormorant Garamond", serif;
    font-size: 11px; letter-spacing: 1px;
  }
</style>
</head>
<body>
<main class="sheet">
  <div class="frame"></div>
  <section class="panel">
    <header class="title">
      <span class="title-ja">骨格分析</span>
      <span class="title-en">make advice sheet</span>
    </header>
    <div class="sheet-no">No.<strong>1</strong></div>
    <div class="rule rule-top"></div>
    <div class="client-name">様</div>
    <div class="rule rule-name"></div>

    <div class="photo-grid">
      <div class="photo-slot slot-a"><span class="label">A</span></div>
      <div class="photo-slot slot-b"><span class="label">B</span></div>
      <div class="photo-slot slot-c"><span class="label">C</span></div>
    </div>

    <p class="notes note-whole"><span class="key">A</span>全体</p>
    <p class="notes note-right"><span class="key">B</span>右顔</p>
    <p class="notes note-left"><span class="key">C</span>左顔</p>
  </section>

  <p class="footer-tag">make advice sheet</p>
  <div class="brand">
    <span class="brand-name">Atelier Rosé</span>
    <span class="brand-line">color styling salon</span>
  </div>
</main>
</body>
</html>
```